New Summit Tile Billboard at HQ

Looking to design a catchy image / theme for a billboard located just above our corporate HQ showroom and warehouse, along the service road of a 6-lane highway. Billboard measures 8ft x 24 ft. Would like to highlight that the store location is directly beneath the sign.

We are a retail and wholesale business selling premium flooring, ready to assemble cabinets, and granite countertops. See image ideas attached. Our information:
NAME: Summit Tile, Cabinets, Countertops
ADDRESS: 417 W. Hwy 82, Duncanville, TX 75284
WEBSITE: www.summittilehub.example
PHONE: 972-8-TILEUP (972-845-3887)

```html
<!DOCTYPE html>
<html lang="en">
<head>
<meta charset="utf-8">
<title>Summit Tile Billboard</title>
<link rel="stylesheet" href="https://fonts.googleapis.com/css2?family=Poppins:wght@400;600;800&family=Montserrat:wght@500&display=swap">
<style>
  :root {
    --page-bg: #e6e7e9;
    --stone-dark: #0b0b0c;
    --stone-mid: #1c1b1a;
    --vein-gold: #b8902f;
    --white: #ffffff;
    --accent-orange: #f26522;
    --url-orange: #f7931e;
  }
  * { margin: 0; padding: 0; box-sizing: border-box; }
  html, body {
    width: 1200px;
    height: 1000px;
    overflow: hidden;
    background: var(--page-bg);
  }
  .billboard {
    position: absolute;
    left: 40px;
    top: 313px;
    width: 1120px;
    height: 373px;
    overflow: hidden;
    color: var(--white);
    font-family: "Poppins", sans-serif;
  }
  .billboard__stone {
    position: absolute;
    inset: 0;
    background:
      linear-gradient(118deg, transparent 30%, rgba(184,144,47,0.18) 40%, transparent 46%),
      linear-gradient(125deg, transparent 55%, rgba(184,144,47,0.14) 62%, transparent 70%),
      radial-gradient(ellipse at 45% 40%, var(--stone-mid) 0%, var(--stone-dark) 70%);
  }
  .billboard__url {
    position: absolute;
    top: 28px;
    right: 26px;
    display: flex;
    align-items: center;
    gap: 8px;
    font-size: 20px;
    font-weight: 600;
    color: var(--url-orange);
  }
  .billboard__url svg { width: 16px; height: 16px; }
  .billboard__content {
    position: absolute;
    left: 0;
    right: 0;
    top: 62px;
    display: flex;
    flex-direction: column;
    align-items: center;
  }
  .brand-name {
    font-size: 106px;
    font-weight: 800;
    line-height: 1;
    letter-spacing: -1px;
    text-transform: uppercase;
  }
  .brand-lines {
    margin-top: 18px;
    width: 804px;
    padding-bottom: 8px;
    border-bottom: 2px solid var(--white);
    display: flex;
    justify-content: space-between;
    align-items: center;
    font-family: "Montserrat", sans-serif;
    font-weight: 500;
    font-size: 30px;
    letter-spacing: 9px;
    text-transform: uppercase;
  }
  .brand-lines__divider {
    width: 2px;
    height: 28px;
    background: var(--white);
    opacity: 0.8;
  }
  .address {
    margin-top: 14px;
    font-size: 25px;
    font-weight: 400;
  }
  .phone-band {
    position: relative;
    margin-top: 22px;
    width: 643px;
    height: 49px;
    display: flex;
    align-items: center;
    justify-content: center;
  }
  .phone-band svg {
    position: absolute;
    inset: 0;
    width: 100%;
    height: 100%;
  }
  .phone-band__text {
    position: relative;
    font-size: 30px;
    font-weight: 600;
    letter-spacing: 0.5px;
  }
</style>
</head>
<body>
  <section class="billboard">
    <div class="billboard__stone" role="img" aria-label="Black granite stone texture with gold veins"></div>

    <div class="billboard__url">
      <svg viewBox="0 0 16 16" aria-hidden="true">
        <path d="M2 14 L12 4" stroke="var(--white)" stroke-width="2"/>
        <path d="M6 3 H13 V10" fill="none" stroke="var(--white)" stroke-width="2"/>
      </svg>
      <span>www.summittilehub.example</span>
    </div>

    <div class="billboard__content">
      <h1 class="brand-name">Summit Tile</h1>
      <div class="brand-lines">
        <span>Cabinets</span>
        <span class="brand-lines__divider"></span>
        <span>Countertops</span>
      </div>
      <p class="address">417 W. Hwy 82, Duncanville, TX 75284</p>
      <div class="phone-band">
        <svg viewBox="0 0 643 49" preserveAspectRatio="none" aria-hidden="true">
          <polygon points="24,0 643,0 619,49 0,49" fill="var(--accent-orange)"/>
        </svg>
        <span class="phone-band__text">972-8-TILEUP (972-845-3887)</span>
      </div>
    </div>
  </section>
</body>
</html>
```